Limbwright Crew of Yuma Bill Board Design

We are a high class full service tree company who specializes in artistic thinning and shaping of trees in Arizona. We want to re brand our company to catch our audiences attention and hook them into calling our company on the spot. We’ve been in business for 30 years and have never truly branded our company. We want our shirts trucks and billboards to match as well as our mailing advertisement so our clientele can recognize us immediately. We are starting with our billboard first and will be following with truck and shirt designs next. Attached is a example of what we are looking for and what we’ve had designed so far. This just isn’t good enough and needs revamped if at all posssible.
- Stencil

```html
<!DOCTYPE html>
<html lang="en">
<head>
<meta charset="utf-8">
<title>Limbwright Crew of Yuma – Billboard</title>
<link href="https://fonts.googleapis.com/css2?family=Cinzel:wght@600;700&family=Montserrat:wght@700;800&family=Oswald:wght@600&display=swap" rel="stylesheet">
<style>
  :root {
    --page-bg: #9a9a9a;
    --board-white: #ffffff;
    --brand-green: #0f9a48;
    --brand-gold: #f2b51c;
    --gold-light: #ffd84a;
    --ink: #1c1a17;
    --leaf-green: #4e7a2c;
    --leaf-dark: #2f4d1c;
    --sky: #a9c9ea;
  }
  * { box-sizing: border-box; margin: 0; padding: 0; }
  html, body { width: 1103px; height: 1200px; overflow: hidden; }
  body { background: var(--page-bg); position: relative; }

  .billboard {
    position: absolute;
    left: 30px; top: 447px;
    width: 1043px; height: 305px;
    background: var(--board-white);
    overflow: hidden;
  }
  .billboard-art { position: absolute; inset: 0; width: 100%; height: 100%; }

  .brand-row {
    position: absolute; left: 392px; top: 44px;
    display: flex; align-items: center; gap: 12px;
  }
  .brand-mark { width: 30px; height: 30px; border-radius: 50%; background: var(--brand-green); flex: none; }
  .brand-name {
    font-family: "Cinzel", serif; font-weight: 600;
    font-size: 20px; letter-spacing: 0.5px; color: var(--ink);
    white-space: nowrap;
  }

  .headline {
    position: absolute; left: 362px; width: 320px; top: 96px;
    text-align: center;
    font-family: "Cinzel", serif; font-weight: 700;
    font-size: 31px; line-height: 36px; color: var(--ink);
  }
  .divider {
    position: absolute; left: 509px; top: 183px;
    width: 27px; height: 4px; background: var(--brand-green);
  }
  .call-label {
    position: absolute; left: 372px; width: 300px; top: 203px;
    text-align: center;
    font-family: "Cinzel", serif; font-weight: 600;
    font-size: 21px; color: var(--ink);
  }
  .phone {
    position: absolute; left: 360px; width: 330px; top: 226px;
    text-align: center;
    font-family: "Oswald", sans-serif; font-weight: 600;
    font-size: 58px; line-height: 64px; color: var(--brand-green);
    letter-spacing: -0.5px;
  }

  .badge-text {
    position: absolute; left: 267px; top: 140px; width: 120px;
    text-align: center; color: var(--ink);
    font-family: "Montserrat", sans-serif; font-weight: 800;
  }
  .badge-number { font-size: 42px; line-height: 40px; }
  .badge-years { font-size: 19px; line-height: 18px; }
  .badge-caption { font-size: 10px; line-height: 11px; font-weight: 700; }
</style>
</head>
<body>
  <section class="billboard">
    <svg class="billboard-art" viewBox="0 0 1712 500" preserveAspectRatio="none">
      <defs>
        <linearGradient id="left-photo-tone" x1="0" y1="0" x2="1" y2="1">
          <stop offset="0" stop-color="var(--sky)"/>
          <stop offset="0.3" stop-color="var(--leaf-green)"/>
          <stop offset="1" stop-color="var(--leaf-dark)"/>
        </linearGradient>
        <linearGradient id="right-photo-tone" x1="0" y1="0" x2="1" y2="1">
          <stop offset="0" stop-color="#3f5a2a"/>
          <stop offset="0.55" stop-color="#6b7a4a"/>
          <stop offset="1" stop-color="#9fbde0"/>
        </linearGradient>
        <linearGradient id="gold-sweep" x1="0" y1="0" x2="0" y2="1">
          <stop offset="0" stop-color="var(--brand-gold)"/>
          <stop offset="0.5" stop-color="var(--gold-light)"/>
          <stop offset="1" stop-color="var(--brand-gold)"/>
        </linearGradient>
      </defs>

      <path class="photo-left" role="img" aria-label="Photo of an arborist in a bucket lift trimming a leafy green tree"
            fill="url(#left-photo-tone)"
            d="M0 0 H470 C570 120 590 360 480 500 H0 Z"/>
      <path class="accent-green" fill="var(--brand-green)"
            d="M510 60 C575 180 600 380 545 500 H480 C555 380 560 210 510 60 Z"/>
      <path class="accent-line" fill="none" stroke="#ffffff" stroke-width="2"
            d="M545 200 C560 330 520 440 420 500"/>

      <path class="accent-gold" fill="url(#gold-sweep)"
            d="M1168 0 H1240 C1150 120 1145 300 1205 470 C1120 330 1118 130 1168 0 Z"/>
      <path class="photo-right" role="img" aria-label="Photo looking up at an arborist in a bucket lift among tall pine branches"
            fill="url(#right-photo-tone)"
            d="M1240 0 H1712 V500 H1250 C1170 370 1160 150 1240 0 Z"/>
      <path class="accent-line" fill="none" stroke="#ffffff" stroke-width="2"
            d="M1320 0 C1230 80 1190 220 1230 340"/>

      <polygon class="experience-badge" fill="url(#gold-sweep)"
        points="537,192 556,225 587,208 591,243 627,240 614,274 647,288 618,310 640,339 605,344 612,379 578,370 570,405 545,381 520,405 512,370 478,379 485,344 450,339 472,310 443,288 476,274 463,240 499,243 503,208 534,225"/>
    </svg>

    <div class="brand-row">
      <span class="brand-mark"></span>
      <span class="brand-name">LIMBWRIGHT CREW</span>
    </div>

    <h1 class="headline">Limbwright Crew<br>of Yuma</h1>
    <div class="divider"></div>
    <p class="call-label">CALL US TODAY</p>
    <p class="phone">928-555-0147</p>

    <div class="badge-text">
      <div class="badge-number">30</div>
      <div class="badge-years">YEARS</div>
      <div class="badge-caption">EXPERIENCE</div>
    </div>
  </section>
</body>
</html>
```